" Empresa jurídica moderna e atuante com foco no segmento empresarial, conta com diferencial de propor uma maior aproximaçao com as empresas/clientes, solucionando seus problemas e prevendo suas necessidades. "

```html
<!DOCTYPE html>
<html lang="pt-BR">
<head>
<meta charset="UTF-8">
<title>Moraes, Teles &amp; Azevedo — Envelopes</title>
<link rel="stylesheet" href="https://fonts.googleapis.com/css2?family=Cinzel:wght@400&family=Open+Sans:wght@400;600&display=swap">
<style>
  :root {
    --bg: #e9e9e7;
    --navy: #34507e;
    --navy-dark: #2a416a;
    --paper: #ffffff;
    --paper-shade: #f1f2f4;
    --ink: #4c5a6e;
    --ink-soft: #7a8596;
    --rule: #c9cdd4;
  }
  * { margin: 0; padding: 0; box-sizing: border-box; }
  html, body { width: 1200px; height: 1200px; overflow: hidden; }
  body { background: var(--bg); position: relative; font-family: "Open Sans", sans-serif; }

  .envelope {
    position: absolute;
    left: 230px;
    width: 740px;
    height: 390px;
    box-shadow: 0 10px 24px rgba(0,0,0,0.18);
  }
  .envelope--back { top: 235px; background: var(--navy); overflow: hidden; }
  .envelope--front {
    top: 650px;
    background: linear-gradient(180deg, var(--paper) 0%, var(--paper-shade) 100%);
  }

  .flap { position: absolute; top: 0; left: 0; width: 740px; height: 130px; }

  .brand {
    position: absolute;
    left: 0; right: 0;
    display: flex;
    flex-direction: column;
    align-items: center;
  }
  .brand__row { display: flex; align-items: center; gap: 12px; }
  .brand__mark { display: block; }
  .brand__name {
    font-family: "Cinzel", serif;
    font-weight: 400;
    letter-spacing: 0.02em;
    white-space: nowrap;
  }
  .brand__tagline {
    font-family: "Cinzel", serif;
    letter-spacing: 0.22em;
    text-transform: uppercase;
    white-space: nowrap;
  }

  .envelope--back .brand { top: 170px; }
  .envelope--back .brand__mark { width: 16px; height: 16px; background: var(--paper); }
  .envelope--back .brand__name { color: var(--paper); font-size: 19px; }
  .envelope--back .brand__tagline {
    color: rgba(255,255,255,0.75);
    font-size: 6.5px;
    margin-top: 5px;
    border-top: 1px solid rgba(255,255,255,0.5);
    padding-top: 3px;
  }

  .contact {
    position: absolute;
    left: 0; right: 0;
    bottom: 26px;
    text-align: center;
    color: var(--paper);
    font-size: 14px;
    line-height: 1.45;
  }
  .contact__web { font-weight: 600; }

  .envelope--front .brand { top: 122px; }
  .envelope--front .brand__mark { width: 34px; height: 34px; background: var(--navy); }
  .envelope--front .brand__name { color: var(--ink); font-size: 38px; }
  .envelope--front .brand__tagline {
    color: var(--ink-soft);
    font-size: 11px;
    margin-top: 8px;
    border-top: 1px solid var(--rule);
    padding-top: 6px;
  }

  .edge-rule {
    position: absolute;
    left: 46px; right: 46px;
    height: 1px;
    background: var(--rule);
    opacity: 0.6;
  }
  .edge-rule--top { top: 40px; }
  .edge-rule--bottom { bottom: 40px; }
</style>
</head>
<body>

  <section class="envelope envelope--back" aria-label="Verso do envelope">
    <svg class="flap" viewBox="0 0 740 130" aria-hidden="true">
      <defs>
        <linearGradient id="flapShade" x1="0" y1="0" x2="0" y2="1">
          <stop offset="0" stop-color="#ffffff"/>
          <stop offset="1" stop-color="#eceef2"/>
        </linearGradient>
      </defs>
      <path d="M0 0 H740 L722 22 Q700 40 660 44 L380 72 Q370 73 360 72 L80 44 Q40 40 18 22 Z"
            fill="rgba(0,0,0,0.25)" transform="translate(0,6)"/>
      <path d="M0 0 H740 L722 22 Q700 40 660 44 L380 72 Q370 73 360 72 L80 44 Q40 40 18 22 Z"
            fill="url(#flapShade)"/>
    </svg>

    <div class="brand">
      <div class="brand__row">
        <span class="brand__mark"></span>
        <span class="brand__name">MORAES, TELES &amp; AZEVEDO</span>
      </div>
      <span class="brand__tagline">Advocacia e Consultoria Jurídica</span>
    </div>

    <address class="contact">
      <div>Tel. 00 (00) 0000-0000</div>
      <div class="contact__web">www.mtaadvocacia.com.br</div>
      <div>End. exemplo dos exemplos I nº 000 I Bairro I Cidade/SP I CEP 00000-00</div>
    </address>
  </section>

  <section class="envelope envelope--front" aria-label="Frente do envelope">
    <span class="edge-rule edge-rule--top"></span>
    <div class="brand">
      <div class="brand__row">
        <span class="brand__mark"></span>
        <span class="brand__name">MORAES, TELES &amp; AZEVEDO</span>
      </div>
      <span class="brand__tagline">Advocacia e Consultoria Jurídica</span>
    </div>
    <span class="edge-rule edge-rule--bottom"></span>
  </section>

</body>
</html>
```